Professional Personal Wordpress Blog Theme

I need a RESPONSIVE design for my personal website at DarrowPlaskett.com that focuses on me as an entrepreneur (CrowdPulse.com, BoutLinker.com, and then the ability to talk about others). My focus on combative sports maybe some still images from this youtube http://vidsharo.example/q7Lm2Xp (possibly in a boxing/muay thai) ring or cage) or a video overlay like on CrowdPulse.com. I very much like the style of CrowdPulse.com but want a real custom feel to my personal blog. MUST INCLUDE views on multiple devices to get the project (desktop, tablet, and smart phone). Think cutting edge/Bleeding edge design for 2015 that focuses on lots of great blog content. No separate categories needed just a really modern homepage and awesome blog layout that has a pro feel while at the same time Brimstoke like (but no skulls and cross bone stuff). If you want to use a background video like on CrowdPulse.com that could work as well. This is a COMPLETE design and theme creation. I need a theme that I can just drop the theme into wordpress if you cannot do the design and then create the theme please do not submit anything.
Updates

Note this is for a full Wordpress theme not just the design. Please do not submit if you aren't also providing a full wordpress theme. Thank you!

Think boxing, kickboxing, muay thai, jiu jitsu, etc.

If you are working on this project or have any questions please let me know. I'm trying to determine if anyone is actively using SketchHive.com because I haven't received any questions or feedback yet. Thanks for taking a look & I hope to find someone to work with soon!

Please check out the files I uploaded to get an idea of what I am looking for. It can deviate but should be something like that if possible (of course it needs to be responsive so some modifications for screen sizes should be made).

In addition to the layout provided in the zip file it would also be good to provide a search bar in the top left of the header (every page) for searching the blog. In addition, easy ways to navigate the site including possibly a nicely designed sitepmap page and related posts on the blog article/single page.

In addition to what I provided (the layouts) I'm also thinking I'd like to see a search layout in the top left of the header and then more creative ways for the site to be navigated (more links) plus, possibly a designed sitemap. Finally, for the responsive portion of the single/blog article page I would want the content of the article to show right below the header and then the sidebar shifted below the article but before the footer.

Target Market(s)

My readers are typically on mobile devices (tablets & smart phones) and in general are other entrepreneurs or martial artists. Fonts should be modern and interesting (not just basic, boring fonts).

Think Rex Dunmore, Hank Bordell, rugged, tough, fighters

Industry/Entity Type

Entrepreneur

Requirements
Must have
• Must be responsive and look great on all devices (desktops, tablets, smart phones). I need a full custom theme that can be dropped right into wordpress. So you must code the theme as well as prepare the design.

Feel free to use pixvault images as I have an account with them.
Nice to have
• Cool modern looking fonts I like the following font (the blog post title here): http://devnotes.quorvix.example/featured/crowdpulse-social-app-sports-enthusiasts-built-quorvix-platform/

The main feature of the site should be blog articles. No need for anything else no poems, videos, etc. Just an awesome blog layout.

The colors should be strong colors Red, Black, Blue, Green, Orange
Should not have
• No cartoons, no unlicensed images (use pixvault please and note the images for me to download in final form). No script looking fonts.

The attached file are just ideas but the flow and concepts should be pretty clear. Please ask if you have any questions.

```html
<!DOCTYPE html>
<html lang="en">
<head>
<meta charset="utf-8">
<title>Darrow Plaskett</title>
<link href="https://fonts.googleapis.com/css2?family=Russo+One&family=Open+Sans:wght@400;600;700&display=swap" rel="stylesheet">
<style>
:root{
  --black:#131313;
  --header:#1a1a1a;
  --section:#222;
  --section-dark:#1c1c1c;
  --tile:#2e2e2e;
  --red:#ff1a00;
  --orange:#f6a100;
  --gold:#f2a31b;
  --white:#fff;
  --muted:#9a9a9a;
  --line:#3a3a3a;
}
*{box-sizing:border-box;margin:0;padding:0}
html,body{width:747px;height:1200px;overflow:hidden;background:var(--black)}
body{position:relative;font-family:"Open Sans",sans-serif;color:var(--white)}
.abs{position:absolute}
.display{font-family:"Russo One",sans-serif;text-transform:uppercase;font-weight:400}

/* header */
.site-header{left:0;top:0;width:747px;height:55px;background:var(--header);border-top:2px solid var(--red)}
.search{left:61px;top:16px;width:151px;height:23px;border:1px solid #444;border-radius:12px;display:flex;align-items:center;padding-left:8px;gap:8px;font-size:7.5px;color:#888}
.brand{left:0;width:747px;top:14px;text-align:center;font-size:22px;letter-spacing:.5px;color:var(--gold)}
.nav{right:61px;top:22px;display:flex;gap:22px;font-size:8.5px;font-weight:700}
.nav .active{color:var(--red)}

/* hero */
.hero{left:0;top:55px;width:747px;height:300px;background:radial-gradient(ellipse at 22% 40%,#8a8a8a 0%,#3a3a3a 30%,#161616 70%),#111}
.play{left:348px;top:145px}
.hero-title{left:0;width:747px;top:205px;text-align:center;font-size:27px;line-height:35px;letter-spacing:1px;text-shadow:0 2px 6px rgba(0,0,0,.6)}
.dots{display:flex;flex-direction:column;gap:4px}
.dots span{width:7px;height:7px;border-radius:50%;background:#777}
.dots span.on{background:transparent;border:1.5px solid var(--red)}
.hero .dots span.on{background:var(--red);border:0}

/* sections */
.portfolio{left:0;top:355px;width:747px;height:225px;background:var(--section)}
.articles{left:0;top:580px;width:747px;height:390px;background:var(--section-dark)}
.section-title{left:0;width:747px;display:flex;justify-content:center;align-items:center;gap:14px;font-size:13.5px;line-height:18px;color:var(--gold);white-space:nowrap}
.section-title .name{color:var(--red)}
.section-title::before,.section-title::after{content:"";display:block;width:60px;height:1px;background:#3c3c3c}

.logos{left:61px;top:77px;display:grid;grid-template-columns:repeat(5,116px);grid-auto-rows:46px;gap:12px 11px}
.logo-tile{background:var(--tile);display:flex;align-items:center;justify-content:center;gap:5px;font-size:10px;font-weight:700;color:#ddd}
.logo-tile i{display:block;width:10px;height:10px;border-radius:50%;background:#ddd}
.logo-tile.more{font-size:8.5px;color:#aaa}

.cards{left:61px;top:81px;display:grid;grid-template-columns:repeat(4,137px);grid-auto-rows:126px;gap:19px 26px}
.card{position:relative;background:#262626;box-shadow:2px 2px 6px rgba(0,0,0,.5);overflow:hidden}
.card .photo{position:absolute;left:0;top:0;width:100%;height:92px}
.card .meta{position:absolute;left:0;bottom:0;width:100%;height:40px;background:rgba(20,20,20,.75);padding:10px 0 0 26px}
.tag{display:flex;align-items:center;gap:5px;font-family:"Russo One",sans-serif;font-size:9px;color:var(--red);text-transform:uppercase}
.date{font-size:5.5px;color:#bbb;margin-left:17px}
.card.text{text-align:center;padding-top:14px}
.card.text .tag{justify-content:center}
.card.text .date{margin:0}
.excerpt{font-size:7px;line-height:10.5px;color:#ccc;padding:13px 14px 0}
.read-more{display:inline-block;margin-top:10px;border:1.5px solid var(--gold);border-radius:9px;font-size:6px;font-weight:700;padding:3px 9px;color:var(--gold)}

/* newsletter */
.newsletter{left:0;top:970px;width:747px;height:60px;background:var(--red)}
.newsletter h3{position:absolute;left:61px;top:21px;font-family:"Russo One",sans-serif;font-size:13px;font-weight:400}
.field{position:absolute;top:19px;height:23px;width:147px;background:#fff;border:1px solid #ddd;font-size:7.5px;color:#777;display:flex;align-items:center;padding-left:5px;gap:5px}
.subscribe{position:absolute;left:601px;top:18px;width:85px;height:25px;border-radius:13px;background:var(--orange);font-weight:700;font-size:9px;display:flex;align-items:center;justify-content:center}

/* footer */
.site-footer{left:0;top:1030px;width:747px;height:170px;background:var(--header)}
.footer-links{left:61px;top:28px;list-style:none;font-size:8px;line-height:15px;color:var(--muted)}
.footer-links li:first-child{color:#fff}
.map{left:166px;top:32px;width:170px;height:100px;background:linear-gradient(135deg,#d9d4c4,#c8c2ae);border:2px solid #eee}
.divider{top:40px;width:1px;height:90px;background:#2f2f2f}
.contact{left:402px;top:30px;font-size:7.5px;line-height:14px;color:var(--muted)}
.contact strong{display:block;font-size:10px;color:#fff;margin-bottom:4px}
.email-btn{left:403px;top:100px;width:64px;height:21px;border-radius:11px;background:var(--red);font-size:8px;font-weight:700;display:flex;align-items:center;justify-content:center}
.socials{left:562px;top:33px;display:flex;gap:3.5px}
.socials span{width:22px;height:22px;border:1.5px solid #ccc;border-radius:50%}
.copyright{right:61px;top:69px;text-align:right;font-size:7.5px;line-height:14px;color:#ddd}
</style>
</head>
<body>

<header class="site-header abs">
  <div class="search abs">
    <svg width="10" height="10" viewBox="0 0 10 10"><circle cx="4" cy="4" r="3" fill="none" stroke="#ddd" stroke-width="1.4"/><line x1="6.2" y1="6.2" x2="9.2" y2="9.2" stroke="#ddd" stroke-width="1.6"/></svg>
    <span>Enter Any keyword</span>
  </div>
  <div class="brand abs display">Darrow Plaskett</div>
  <nav class="nav abs"><span class="active">HOME</span><span>BLOG</span><span>CONTACT ME</span></nav>
</header>

<section class="hero abs" role="img" aria-label="Black and white boxing ring with bell and light rays behind a cross">
  <svg class="play abs" width="50" height="50" viewBox="0 0 50 50"><circle cx="25" cy="25" r="23.5" fill="none" stroke="rgba(255,255,255,.35)" stroke-width="2"/><path d="M20 15 L34 25 L20 35Z" fill="rgba(255,255,255,.35)"/></svg>
  <h1 class="hero-title abs display">Fight the good fight and<br>forgive or forget the rest</h1>
  <div class="dots abs" style="left:719px;top:133px"><span class="on"></span><span></span><span></span></div>
</section>

<section class="portfolio abs">
  <h2 class="section-title abs display" style="top:36px"><span>Portfolio Companies - <span class="name">Darrow Plaskett</span></span></h2>
  <div class="logos abs">
    <div class="logo-tile"><i></i>BoutLinker</div>
    <div class="logo-tile"><i></i>CrowdPulse</div>
    <div class="logo-tile">Ledgerwise</div>
    <div class="logo-tile">Tallyforge.com</div>
    <div class="logo-tile">Brightmark</div>
    <div class="logo-tile">VNT</div>
    <div class="logo-tile"><i></i>Keystead</div>
    <div class="logo-tile">Harrowgate</div>
    <div class="logo-tile">Pinecrest.com</div>
    <div class="logo-tile more">MANY MORE...</div>
  </div>
  <div class="dots abs" style="left:719px;top:103px"><span></span><span class="on"></span><span></span></div>
</section>

<section class="articles abs">
  <h2 class="section-title abs display" style="top:33px"><span>Articles &amp; More by - <span class="name">Darrow Plaskett</span></span></h2>
  <div class="cards abs">
    <article class="card"><div class="photo" role="img" aria-label="Boxer in gloves on dark background" style="background:linear-gradient(160deg,#5a4a40,#1e1e1e)"></div><div class="meta"><div class="tag"><svg width="11" height="9" viewBox="0 0 11 9"><path d="M1 1.5 Q3 .5 5.5 2 V8 Q3 6.5 1 7.5Z M10 1.5 Q8 .5 5.5 2 V8 Q8 6.5 10 7.5Z" fill="none" stroke="var(--gold)" stroke-width=".9"/></svg>Think Boxing</div><div class="date">2 days Ago</div></div></article>
    <article class="card text"><div class="tag"><svg width="11" height="9" viewBox="0 0 11 9"><path d="M1 1.5 Q3 .5 5.5 2 V8 Q3 6.5 1 7.5Z M10 1.5 Q8 .5 5.5 2 V8 Q8 6.5 10 7.5Z" fill="none" stroke="var(--gold)" stroke-width=".9"/></svg>Kickboxing</div><div class="date">2 days Ago</div><p class="excerpt">Sed ut perspiciatis unde omnis istlorem e natus error sit voluptatem aloreccus.</p><span class="read-more">READ MORE</span></article>
    <article class="card"><div class="photo" role="img" aria-label="Muay thai fighter throwing a high knee" style="background:linear-gradient(160deg,#3a3a3a,#151515)"></div><div class="meta"><div class="tag"><svg width="11" height="9" viewBox="0 0 11 9"><path d="M1 1.5 Q3 .5 5.5 2 V8 Q3 6.5 1 7.5Z M10 1.5 Q8 .5 5.5 2 V8 Q8 6.5 10 7.5Z" fill="none" stroke="var(--gold)" stroke-width=".9"/></svg>Muay Thai</div><div class="date">2 days Ago</div></div></article>
    <article class="card"><div class="photo" role="img" aria-label="Two fighters exchanging kicks in a ring" style="background:linear-gradient(160deg,#5b6470,#2a2d33)"></div><div class="meta"><div class="tag"><svg width="11" height="9" viewBox="0 0 11 9"><path d="M1 1.5 Q3 .5 5.5 2 V8 Q3 6.5 1 7.5Z M10 1.5 Q8 .5 5.5 2 V8 Q8 6.5 10 7.5Z" fill="none" stroke="var(--gold)" stroke-width=".9"/></svg>Jiu Jitsu</div><div class="date">2 days Ago</div></div></article>
    <article class="card"><div class="photo" role="img" aria-label="Boxer in guard stance" style="background:linear-gradient(160deg,#4a4a4a,#171717)"></div><div class="meta"><div class="tag"><svg width="11" height="9" viewBox="0 0 11 9"><path d="M1 1.5 Q3 .5 5.5 2 V8 Q3 6.5 1 7.5Z M10 1.5 Q8 .5 5.5 2 V8 Q8 6.5 10 7.5Z" fill="none" stroke="var(--gold)" stroke-width=".9"/></svg>Think Boxing</div><div class="date">2 days Ago</div></div></article>
    <article class="card"><div class="photo" role="img" aria-label="Fighter in a clinch on the mat" style="background:linear-gradient(160deg,#6b4c38,#2b1f18)"></div><div class="meta"><div class="tag"><svg width="11" height="9" viewBox="0 0 11 9"><path d="M1 1.5 Q3 .5 5.5 2 V8 Q3 6.5 1 7.5Z M10 1.5 Q8 .5 5.5 2 V8 Q8 6.5 10 7.5Z" fill="none" stroke="var(--gold)" stroke-width=".9"/></svg>Muay Thai</div><div class="date">2 days Ago</div></div></article>
    <article class="card"><div class="photo" role="img" aria-label="Two grapplers in a hold against white background" style="background:linear-gradient(160deg,#e8e8e8,#9a9a9a)"></div><div class="meta"><div class="tag"><svg width="11" height="9" viewBox="0 0 11 9"><path d="M1 1.5 Q3 .5 5.5 2 V8 Q3 6.5 1 7.5Z M10 1.5 Q8 .5 5.5 2 V8 Q8 6.5 10 7.5Z" fill="none" stroke="var(--gold)" stroke-width=".9"/></svg>Kickboxing</div><div class="date">2 days Ago</div></div></article>
    <article class="card"><div class="photo" role="img" aria-label="Silhouette flying kick on a beach at sunset" style="background:linear-gradient(180deg,#b9c7bf,#e9d9a0 55%,#8d8a6a)"></div><div class="meta"><div class="tag"><svg width="11" height="9" viewBox="0 0 11 9"><path d="M1 1.5 Q3 .5 5.5 2 V8 Q3 6.5 1 7.5Z M10 1.5 Q8 .5 5.5 2 V8 Q8 6.5 10 7.5Z" fill="none" stroke="var(--gold)" stroke-width=".9"/></svg>Jiu Jitsu</div><div class="date">2 days Ago</div></div></article>
  </div>
  <div class="dots abs" style="left:719px;top:187px"><span></span><span></span><span class="on"></span></div>
</section>

<section class="newsletter abs">
  <h3>SUBSCRIBE TO MY NEWSLETTER</h3>
  <div class="field" style="left:286px">Name:</div>
  <div class="field" style="left:442px"><svg width="10" height="7" viewBox="0 0 10 7"><rect x=".5" y=".5" width="9" height="6" fill="#aaa"/><path d="M.5 .5 L5 4 L9.5 .5" fill="none" stroke="#fff" stroke-width=".8"/></svg>Email:</div>
  <div class="subscribe">SUBSCRIBE</div>
</section>

<footer class="site-footer abs">
  <ul class="footer-links abs"><li>Home</li><li>Site Map</li><li>About</li><li>Blog</li><li>Contact</li></ul>
  <div class="map abs" role="img" aria-label="Street map showing the office location"></div>
  <div class="divider abs" style="left:367px"></div>
  <div class="divider abs" style="left:518px"></div>
  <div class="contact abs"><strong>darrowplaskett</strong>(415) 555-0142<br>1840 Larkspur Ave, Ste 410<br>Easton, Tx 77012</div>
  <div class="email-btn abs">EMAIL ME</div>
  <div class="socials abs"><span></span><span></span><span></span><span></span><span></span></div>
  <div class="copyright abs">Copyright © 2015 darrowplaskett.com<br>All rights reserved</div>
</footer>

</body>
</html>
```